Harborlight Equity Corporate Profile

Redesign Corporate Profile with special attention to Cover, Dividers, Introduction of professional images, icons, colors, formatting among others. To visually enhance the 24 pages to give it a financial look with a young and fresh angle.
The PPT is a corporate profile which is a presentation about the company, its key milestones along with specific key case studies.
Images related to Dubai city, millennial consumer, globalization, technology should be included.
Target Market(s)
Investors, Brand Owners, Shareholders, Employees
Industry/Entity Type
Investment Advisory
Requirements
Must have
- Maintain current content and section structure
- Enhance cover, dividers
- Add professional images
- Enhance graphs and charts
- Add info-graphics

```html
<!DOCTYPE html>
<html lang="en">
<head>
<meta charset="utf-8">
<title>Harborlight Equity – Corporate Profile</title>
<link href="https://fonts.googleapis.com/css2?family=Roboto:wght@300;400;500;700&display=swap" rel="stylesheet">
<style>
:root{
  --red:#d7262b;
  --red-dark:#9e1519;
  --ink:#1c1c1d;
  --ink-2:#2b2b2d;
  --grey:#7b7b7d;
  --light:#e9e9ea;
  --paper:#ffffff;
  --page:#f4f4f4;
}
*{box-sizing:border-box;margin:0;padding:0}
html,body{width:777px;height:1200px;overflow:hidden;background:var(--page);font-family:"Roboto",Arial,sans-serif;color:var(--ink)}
.deck{position:relative;width:777px;height:1200px;padding:3px 6px}
.row{display:flex;gap:5px;margin-bottom:7px;justify-content:center}
.slide{position:relative;width:252px;height:141px;background:var(--paper);overflow:hidden;box-shadow:0 0 0 .5px #d4d4d4}
.slide.dark{background:var(--ink);color:#fff}
.title{position:absolute;left:7px;top:6px;font-size:7px;font-weight:700;color:var(--ink)}
.dark .title{color:#fff}
.foot{position:absolute;left:6px;right:6px;bottom:3px;display:flex;justify-content:space-between;align-items:center;font-size:2.6px;color:var(--red)}
.foot .mark{font-size:3px;color:var(--ink);font-weight:700;letter-spacing:.3px}
.dark .foot .mark{color:#fff}
.brand{display:flex;align-items:center;gap:3px;font-weight:500;letter-spacing:.8px;color:#fff}
.brand .sq{width:9px;height:9px;border:1px solid #fff}
.photo{position:absolute}
.ph-city{background:linear-gradient(135deg,#3a3a3e,#17171a 60%,#2c2a2a)}
.ph-crowd{background:linear-gradient(160deg,#4a4340,#1d1b1b 70%)}
.band{position:absolute;background:linear-gradient(180deg,var(--red),var(--red-dark))}
.t{font-size:3px;line-height:1.35;color:#555}
.dark .t{color:#ccc}
.red{color:var(--red)}
.abs{position:absolute}
.divider .sec{position:absolute;left:0;top:86px;width:155px;height:26px;padding:3px 8px;background:rgba(20,20,20,.85)}
.divider .sec b{display:block;font-size:10px;font-weight:700;color:#fff}
.divider .sec span{display:block;font-size:5px;font-weight:500;color:var(--red);letter-spacing:.3px}
.divider .stripe{position:absolute;left:155px;right:0;top:86px;height:26px;background:var(--red)}
.divider .brand{position:absolute;right:14px;top:12px;font-size:5px}
.stat{position:absolute;display:flex;align-items:center;gap:6px;font-size:5px;color:#fff}
.stat b{color:var(--red);font-size:9px;font-weight:500;min-width:14px;text-align:center}
.nbar{position:absolute;height:17px;display:flex;align-items:center}
.nbar .n{width:16px;height:100%;background:var(--ink);color:#fff;font-size:7px;display:flex;align-items:center;justify-content:center}
.nbar .d{flex:1;height:100%;background:var(--red);padding:2px 4px}
.nbar .d.alt{background:var(--ink-2)}
.nbar .d .t{color:#fff;font-size:2.6px}
.person{position:absolute;width:30px;text-align:center;font-size:2.6px;line-height:1.2}
.person .pic{width:26px;height:25px;margin:0 auto 2px;background:linear-gradient(180deg,#b9b9bb,#6a6a6c)}
.person b{display:block;font-size:2.8px}
.icn{position:absolute;width:40px;text-align:center}
.icn .red{font-size:3.2px;font-weight:700}
.rtile{position:absolute;height:16px;background:var(--red);color:#fff;font-size:3px;display:flex;align-items:center;justify-content:center;text-align:center}
.tile{position:absolute;width:52px;height:38px;background:var(--light);text-align:center;padding-top:6px}
.tile b{display:block;color:var(--red);font-size:9px;font-weight:500}
.tile.dk b{color:var(--ink)}
.tile span{display:block;font-size:3px;color:#444;line-height:1.2}
.logo-box{position:absolute;width:23px;height:12px;background:var(--light)}
.circ{position:absolute;width:13px;height:13px;border-radius:50%;background:var(--red);border:1.5px solid #fff;box-shadow:0 0 0 .5px var(--red)}
</style>
</head>
<body>
<main class="deck">

<div class="row">
  <section class="slide dark">
    <div class="photo ph-city" style="left:0;top:0;width:252px;height:141px" role="img" aria-label="Dim city skyline at night"></div>
    <div class="band" style="left:118px;top:0;width:40px;height:141px;opacity:.9"></div>
    <div class="brand abs" style="left:18px;top:66px;font-size:5px"><span class="sq"></span>HARBORLIGHT</div>
    <div class="abs" style="left:124px;top:62px;color:#fff">
      <div style="font-size:9px;font-weight:700">HARBORLIGHT EQUITY</div>
      <div style="font-size:5.5px">Global Growth with Local Expertise</div>
      <div style="margin-top:4px;background:var(--red);font-size:3px;padding:1px 3px;display:inline-block">October 2017</div>
    </div>
  </section>
  <section class="slide dark">
    <div class="photo ph-city" style="left:0;top:0;width:140px;height:141px" role="img" aria-label="Office interior in dark tones"></div>
    <div class="brand abs" style="left:14px;top:46px;font-size:5px"><span class="sq"></span>HARBORLIGHT</div>
    <div class="abs" style="left:14px;top:70px;width:105px;font-size:3.5px;font-style:italic;color:#ddd;line-height:1.35">"Our investment approach focuses on partnering with brands which are in the roll-out phase that require capital and local expertise to successfully enter and grow in international markets"</div>
    <div class="abs" style="left:14px;top:108px;font-size:3.5px;color:#ccc">Lara Venn Founder &amp; CEO</div>
    <div class="band" style="left:140px;top:0;width:112px;height:141px"></div>
    <div class="abs" style="left:157px;top:32px;font-size:9px;color:#fff">AGENDA</div>
    <div class="abs" style="left:150px;top:55px;font-size:3.6px;color:#fff;line-height:3">
      1&nbsp;&nbsp;&nbsp;About Harborlight Equity<br>2&nbsp;&nbsp;&nbsp;Our Investments<br>3&nbsp;&nbsp;&nbsp;Why Partnering With Us<br>4&nbsp;&nbsp;&nbsp;Millennial Consumer Opportunity
    </div>
  </section>
  <section class="slide dark divider">
    <div class="photo ph-city" style="left:0;top:0;width:252px;height:141px" role="img" aria-label="Modern tower skyline"></div>
    <div class="brand"><span class="sq"></span>HARBORLIGHT</div>
    <div class="sec"><b>SECTION 1 :</b><span>ABOUT HARBORLIGHT EQUITY</span></div>
    <div class="stripe"></div>
  </section>
</div>

<div class="row">
  <section class="slide dark">
    <div class="title" style="font-size:6.5px;top:7px">HARBORLIGHT EQUITY AT A GLANCE</div>
    <div class="abs" style="left:0;right:0;top:18px;height:1px;background:#444"></div>
    <div class="stat" style="left:8px;top:28px"><b>5</b>Reputable Private Equity<br>Investors from GCC</div>
    <div class="stat" style="left:8px;top:58px"><b>10</b>Experienced Management<br>Professionals in Dubai</div>
    <div class="stat" style="left:8px;top:88px"><b>2</b>Completed Investments<br>Over Last 12 Months</div>
    <div class="stat" style="left:126px;top:28px"><b>10%</b>Dividend Yield After 18<br>Months of Operations</div>
    <div class="stat" style="left:126px;top:58px"><b>2x</b>Unrealized Cash on Cash<br>Return Since Inception</div>
    <div class="stat" style="left:126px;top:88px"><b>4</b>Operating Markets - UAE,<br>Saudi Arabia, South Africa<br>and Qatar</div>
    <div class="foot"><span class="mark">HARBORLIGHT</span><span style="color:#bbb">© Copyright 2017 HARBORLIGHT EQUITY. All rights reserved.</span></div>
  </section>
  <section class="slide">
    <div class="title">About Harborlight Equity</div>
    <div class="abs" style="left:7px;top:20px;font-size:3.5px;font-weight:700">Harborlight Equity Key Markets Coverage</div>
    <div class="photo" style="left:6px;top:28px;width:72px;height:80px;background:linear-gradient(160deg,#c9c9cb,#8d8d90)" role="img" aria-label="Map of Africa and the Middle East with key markets highlighted in red"></div>
    <div class="abs" style="left:88px;top:17px;width:36px;height:40px;background:#f0f0f0;padding:3px"><div class="t">Targets fundamental shifts in consumer behavior</div></div>
    <div class="abs" style="left:127px;top:17px;width:36px;height:40px;background:var(--red);padding:3px"><div class="t" style="color:#fff">Provides growth capital to companies in the roll-out stage</div></div>
    <div class="abs" style="left:166px;top:17px;width:36px;height:40px;background:#f0f0f0;padding:3px"><div class="t">Partners with strong brand management teams</div></div>
    <div class="abs" style="left:205px;top:17px;width:38px;height:40px;background:#f0f0f0;padding:3px"><div class="t">Develops and executes regional and multi-channel expansion</div></div>
    <div class="abs t" style="left:88px;top:63px;width:72px">Global Access, Local Resources. Global network provides access to emerging opportunities which are proprietary. Our local team is experienced in developing local fit operating models.</div>
    <div class="abs t" style="left:166px;top:63px;width:76px">Our Partnerships Come First. Focused value add investor with aligned objectives with partner brand. Develop and enhance brand positioning, retail channels and regional partnerships.</div>
    <div class="foot"><span class="mark">HARBORLIGHT</span><span>© Copyright 2017 HARBORLIGHT EQUITY. All rights reserved.</span></div>
  </section>
  <section class="slide">
    <div class="title">Global Growth with Local Expertise: Harborlight Solution</div>
    <div class="nbar" style="left:7px;top:20px;width:148px;height:12px"><div class="n" style="width:12px;font-size:5px">1</div><div class="d alt"><div class="t">International brands are looking to expand into emerging markets to boost gross profit margins</div></div></div>
    <div class="nbar" style="left:7px;top:34px;width:148px;height:12px"><div class="n" style="width:12px;font-size:5px">2</div><div class="d alt"><div class="t">Shelf space is limited in developed markets for emerging brands due to competition</div></div></div>
    <div class="nbar" style="left:7px;top:48px;width:148px;height:12px"><div class="n" style="width:12px;font-size:5px">3</div><div class="d"><div class="t">Expansion in emerging markets is an attractive capital proposition which can be risky</div></div></div>
    <div class="abs" style="left:7px;top:64px;font-size:3.3px;font-weight:700">Illustrative Overview of Retail Growth Phases</div>
    <svg class="abs" style="left:7px;top:70px" width="150" height="52" viewBox="0 0 150 52">
      <polyline points="5,48 40,44 75,36 110,22 145,6" fill="none" stroke="#555" stroke-width=".8"/>
      <rect x="2" y="40" width="30" height="10" fill="#e4e4e4"/><rect x="38" y="32" width="30" height="18" fill="#e4e4e4"/>
      <rect x="74" y="22" width="30" height="28" fill="#e4e4e4"/><rect x="110" y="10" width="30" height="40" fill="#e4e4e4"/>
      <text x="4" y="47" font-size="3" fill="#333">STAGE 1</text><text x="40" y="47" font-size="3" fill="#333">STAGE 2</text>
      <text x="76" y="47" font-size="3" fill="#333">STAGE 3</text><text x="112" y="47" font-size="3" fill="#333">STAGE 4</text>
      <path d="M80 34 L100 34" stroke="var(--red)" stroke-width="1.5"/>
    </svg>
    <div class="abs" style="left:162px;top:19px;width:84px;height:104px;border:.6px solid var(--red);padding:3px">
      <div style="font-size:3.2px;font-weight:700;color:var(--red)">Key Benefits for Retail Brand</div>
      <div class="t">✓ Fully funded expansion into new markets<br>✓ Decreased operating risk by partnering<br>✓ Access to tier 1 retail locations<br>✓ Expansion of global marketing</div>
      <div style="font-size:3.2px;font-weight:700;color:var(--red);margin-top:4px">Key Benefits for Harborlight Equity</div>
      <div class="t">✓ Access to emerging brands looking at MENA<br>✓ Partner with a successful brand with a proven model<br>✓ Option to scale up through corporate development<br>✓ Locally adapted marketing and branding</div>
    </div>
    <div class="foot"><span class="mark">HARBORLIGHT</span><span>© Copyright 2017 HARBORLIGHT EQUITY. All rights reserved.</span></div>
  </section>
</div>

<div class="row">
  <section class="slide">
    <div class="title">How Does Harborlight Turn Opportunity into Business Case?</div>
    <div class="abs" style="left:7px;top:18px;font-size:3.3px;font-weight:700">3 key elements are fundamental to Harborlight Equity value creation approach</div>
    <div class="nbar" style="left:7px;top:27px;width:238px;height:28px"><div class="n" style="width:40px;background:#111"><svg width="12" height="12" viewBox="0 0 12 12"><path d="M2 10 L6 2 L10 10 Z" fill="none" stroke="#fff" stroke-width=".8"/></svg></div><div class="n" style="width:38px;font-size:3.3px;background:var(--ink-2)">1&nbsp; Access to Emerging Markets</div><div class="d alt"><div class="t">Access to highly attractive retail developing countries such as UAE, Saudi Arabia, Kuwait, Qatar, Nigeria, South Africa among others. Our team is on the ground with deep regional knowledge.</div></div></div>
    <div class="nbar" style="left:7px;top:58px;width:238px;height:28px"><div class="n" style="width:40px;background:#111"><svg width="12" height="12" viewBox="0 0 12 12"><circle cx="5" cy="5" r="3.5" fill="none" stroke="#fff" stroke-width=".8"/><path d="M7.5 7.5 L11 11" stroke="#fff" stroke-width=".8"/></svg></div><div class="n" style="width:38px;font-size:3.3px;background:var(--red)">2&nbsp; Local Capital</div><div class="d alt"><div class="t">Harborlight Equity funds market entry, development of business network and sales channels for the partner brands through the establishment of local companies.</div></div></div>
    <div class="nbar" style="left:7px;top:89px;width:238px;height:28px"><div class="n" style="width:40px;background:var(--red)"><svg width="12" height="12" viewBox="0 0 12 12"><rect x="2" y="2" width="8" height="8" fill="none" stroke="#fff" stroke-width=".8"/></svg></div><div class="n" style="width:38px;font-size:3.3px;background:var(--red-dark)">3&nbsp; Professional Management</div><div class="d"><div class="t">A qualified team of professionals with sector specific expertise across strategy, branding, marketing, online and social media activations, financial management.</div></div></div>
    <div class="foot"><span class="mark">HARBORLIGHT</span><span>© Copyright 2017 HARBORLIGHT EQUITY. All rights reserved.</span></div>
  </section>
  <section class="slide">
    <div class="title">Harborlight Founding Team Members</div>
    <div class="person" style="left:8px;top:20px"><div class="pic" role="img" aria-label="Portrait photo"></div><b>Omar Haddad</b>Chairman<br>30 years of investing</div>
    <div class="person" style="left:55px;top:20px"><div class="pic" role="img" aria-label="Portrait photo"></div><b>Lara Venn</b><span class="red">Founder &amp; CEO</span><br>18 years private equity</div>
    <div class="person" style="left:102px;top:20px"><div class="pic" role="img" aria-label="Portrait photo"></div><b>Rohan Mehta</b><span class="red">Board Member</span><br>26 years private equity</div>
    <div class="person" style="left:149px;top:20px"><div class="pic" role="img" aria-label="Portrait photo"></div><b>Ilse Brandt</b><span class="red">Director</span><br>16 years luxury retail</div>
    <div class="person" style="left:196px;top:20px"><div class="pic" role="img" aria-label="Portrait photo"></div><b>Peter Odhiambo</b><span class="red">Brand Manager</span><br>5 years retail</div>
    <div class="person" style="left:8px;top:74px"><div class="pic" role="img" aria-label="Portrait photo"></div><b>Karim Saleh</b><span class="red">Board Member</span><br>20 years hospitality</div>
    <div class="person" style="left:55px;top:74px"><div class="pic" role="img" aria-label="Portrait photo"></div><b>Nadia Farouk</b><span class="red">Senior Associate</span><br>6 years private equity</div>
    <div class="person" style="left:102px;top:74px"><div class="pic" role="img" aria-label="Portrait photo"></div><b>Priya Lal</b><span class="red">Analyst</span><br>3 years finance</div>
    <div class="person" style="left:149px;top:74px"><div class="pic" role="img" aria-label="Portrait photo"></div><b>Daniel Cruz</b><span class="red">Retail Manager</span><br>8 years retail</div>
    <div class="person" style="left:196px;top:74px"><div class="pic" role="img" aria-label="Portrait photo"></div><b>Marta Rossi</b><span class="red">Retail Partner</span><br>20 years branding</div>
    <div class="foot"><span class="mark">HARBORLIGHT</span><span>© Copyright 2017 HARBORLIGHT EQUITY. All rights reserved.</span></div>
  </section>
  <section class="slide">
    <div class="title">Harborlight Approach to Sustainable Business</div>
    <svg class="abs" style="left:0;top:0" width="252" height="60" viewBox="0 0 252 60">
      <g fill="none" stroke="var(--red)" stroke-width=".8">
        <rect x="27" y="28" width="3" height="8"/><rect x="32" y="24" width="3" height="12"/><rect x="37" y="20" width="3" height="16"/>
        <circle cx="80" cy="26" r="3"/><circle cx="86" cy="26" r="3"/><path d="M75 36 Q80 30 85 36 Q90 30 95 36"/>
        <circle cx="128" cy="28" r="6"/><path d="M128 22 V34 M122 28 H134"/>
        <path d="M166 32 L172 26 L178 32 L184 26"/><path d="M166 22 H184"/>
        <circle cx="220" cy="26" r="5"/><path d="M216 31 L214 38 L220 35 L226 38 L224 31"/>
      </g>
    </svg>
    <div class="icn" style="left:12px;top:40px"><div class="red">Economic Impact</div><div class="t">We strive to have a positive impact for our shareholders and partners</div></div>
    <div class="icn" style="left:62px;top:40px"><div class="red">Work Ethics</div><div class="t">We have a strong work culture where we aim for best practice</div></div>
    <div class="icn" style="left:108px;top:40px"><div class="red">Empowerment</div><div class="t">We provide employment to young people and train local staff</div></div>
    <div class="icn" style="left:155px;top:40px"><div class="red">Fair Business</div><div class="t">We treat our shareholders and suppliers with honesty</div></div>
    <div class="icn" style="left:200px;top:40px"><div class="red">Commitment</div><div class="t">We remain committed to excellence and long term growth</div></div>
    <div class="rtile" style="left:12px;top:96px;width:40px">Group's net profit margin of 25%</div>
    <div class="rtile" style="left:58px;top:96px;width:40px">10% Dividend Yield for 2017</div>
    <div class="rtile" style="left:106px;top:96px;width:40px">75% female workforce</div>
    <div class="rtile" style="left:152px;top:96px;width:40px">+/-5% Budget variations for 2017</div>
    <div class="rtile" style="left:198px;top:96px;width:42px">7 to 10 years average business commitment</div>
    <div class="foot"><span class="mark">HARBORLIGHT</span><span>© Copyright 2017 HARBORLIGHT EQUITY. All rights reserved.</span></div>
  </section>
</div>

<div class="row">
  <section class="slide dark divider">
    <div class="photo ph-city" style="left:0;top:0;width:252px;height:141px" role="img" aria-label="Aerial view of city towers at dusk"></div>
    <div class="brand"><span class="sq"></span>HARBORLIGHT</div>
    <div class="sec"><b>SECTION 2 :</b><span>OUR INVESTMENTS</span></div>
    <div class="stripe"></div>
  </section>
  <section class="slide">
    <div class="title">Harborlight Corporate Structure at a Glance</div>
    <div class="abs t" style="left:7px;top:17px;width:236px;color:#333">Harborlight Equity is a venture investment holding company focusing on providing capital and expertise to retail and consumer products brands. The group controls and operates various legal entities including Harborlight Partners &amp; Co, Harborlight Footwear and Harborlight Cosmetics.</div>
    <div class="abs" style="left:10px;top:34px;width:60px;height:86px;border:.6px solid #999">
      <div style="background:var(--ink);color:#fff;font-size:3px;padding:2px">Harborlight Partners &amp; Co</div>
      <div class="t" style="padding:3px">Harborlight Partners &amp; Co is a subsidiary of Harborlight Equity Ltd. The entity focuses on investment advisory services including market studies, sector research and insights, equity and debt raising and corporate strategy.</div>
    </div>
    <svg class="abs" style="left:72px;top:68px" width="18" height="14"><path d="M0 4 H10 V0 L18 7 L10 14 V10 H0 Z" fill="var(--red)"/></svg>
    <div class="abs" style="left:92px;top:34px;width:64px;height:86px;border:.6px solid #999">
      <div style="background:var(--ink);color:#fff;font-size:3px;padding:2px">Harborlight Footwear</div>
      <div class="t" style="padding:3px">Harborlight Urban Footwear is a subsidiary of Harborlight Equity. The operational vehicle for footwear brand rights in GCC, India, Southern Africa and Egypt. Stores and e-commerce operations with 18 employees.</div>
    </div>
    <svg class="abs" style="left:158px;top:68px" width="18" height="14"><path d="M0 4 H10 V0 L18 7 L10 14 V10 H0 Z" fill="var(--red)"/></svg>
    <div class="abs" style="left:178px;top:34px;width:64px;height:86px;border:.6px solid #999">
      <div style="background:var(--ink);color:#fff;font-size:3px;padding:2px">Harborlight Cosmetics</div>
      <div class="t" style="padding:3px">Harborlight Cosmetics is a subsidiary of Harborlight Equity. Holds exclusive rights for a cosmetics brand in UAE, Saudi Arabia, Kuwait and Qatar. 10 retail stores and 20 employees.</div>
    </div>
    <div class="foot"><span class="mark">HARBORLIGHT</span><span>© Copyright 2017 HARBORLIGHT EQUITY. All rights reserved.</span></div>
  </section>
  <section class="slide">
    <div class="title">Harborlight Partners &amp; Co Management Approach</div>
    <svg class="abs" style="left:0;top:0" width="252" height="141" viewBox="0 0 252 141">
      <g fill="none" stroke="var(--red)" stroke-width=".8">
        <circle cx="20" cy="36" r="6"/><circle cx="20" cy="36" r="2"/>
        <path d="M14 70 L20 62 L26 70 Z"/><circle cx="20" cy="98" r="6"/><path d="M17 98 H23"/>
        <path d="M132 30 L142 40 M132 40 L142 30"/><path d="M130 66 Q137 58 144 66 Q137 74 130 66"/><rect x="131" y="92" width="12" height="10"/>
      </g>
    </svg>
    <div class="abs t" style="left:34px;top:28px;width:88px">Fully integrated investment management with focus on venture development. We identify, source and work with the fastest growing brands globally.</div>
    <div class="abs t" style="left:34px;top:60px;width:88px">Deep expertise in market entry strategies with an established track record. We develop best fit operating models to succeed in local markets.</div>
    <div class="abs t" style="left:34px;top:92px;width:88px">Experienced financial management backed by consistent development funding. We forecast, monitor and report revenues and ROE.</div>
    <div class="abs t" style="left:150px;top:28px;width:92px">Disciplined market analysis to enable pricing decisions. We follow omni-channel strategies to boost volume and support growth.</div>
    <div class="abs t" style="left:150px;top:60px;width:92px">Access to the key locations in local markets due to extensive relationships with real operators and developers.</div>
    <div class="abs t" style="left:150px;top:92px;width:92px">Dedicated social media and marketing to enable strong brand positioning and integrated marketing and public relation campaigns.</div>
    <div class="foot"><span class="mark">HARBORLIGHT</span><span>© Copyright 2017 HARBORLIGHT EQUITY. All rights reserved.</span></div>
  </section>
</div>

<div class="row">
  <section class="slide">
    <div class="title">Category Investment: Harborlight Footwear</div>
    <div class="abs" style="left:9px;top:22px;font-size:6px;font-weight:700;letter-spacing:1px">TORVIK</div>
    <div class="abs t" style="left:40px;top:20px;width:60px">TORVIK manufactures, sells and distributes branded footwear products targeting millennial consumers. The brand has a strong global presence.</div>
    <div class="photo" style="left:7px;top:50px;width:100px;height:55px;background:linear-gradient(160deg,#cfcfd1,#9a9a9c)" role="img" aria-label="World map marking existing and new markets"></div>
    <div class="abs" style="left:160px;top:17px;font-size:3.5px;font-weight:700">Value Creation for TORVIK Footwear</div>
    <svg class="abs" style="left:118px;top:24px" width="130" height="80" viewBox="0 0 130 80">
      <line x1="10" y1="74" x2="125" y2="74" stroke="#999" stroke-width=".5"/>
      <rect x="78" y="34" width="14" height="40" fill="var(--red)"/>
      <rect x="100" y="14" width="14" height="44" fill="var(--red)"/><rect x="100" y="58" width="14" height="16" fill="#444"/>
      <text x="80" y="31" font-size="3" fill="var(--red)">15,000</text><text x="102" y="11" font-size="3" fill="var(--red)">20,000</text>
      <path d="M84 20 Q95 4 106 8" stroke="#777" stroke-width=".5" fill="none"/><text x="88" y="6" font-size="3">+40%</text>
      <text x="8" y="40" font-size="3" fill="var(--red)">Footwear sales</text><text x="8" y="56" font-size="3" fill="#d77">Store sales</text>
    </svg>
    <div class="abs" style="left:110px;top:110px;width:136px;height:17px;background:var(--ink);display:flex;justify-content:space-around;align-items:center;color:#fff;font-size:5px">
      <span>10<small style="font-size:2.5px"> Markets</small></span><span>50+<small style="font-size:2.5px"> Employees</small></span><span>15<small style="font-size:2.5px"> Stores</small></span><span>2<small style="font-size:2.5px"> Partners</small></span>
    </div>
    <div class="foot"><span class="mark">HARBORLIGHT</span><span>© Copyright 2017 HARBORLIGHT EQUITY. All rights reserved.</span></div>
  </section>
  <section class="slide">
    <div class="title">Category Investments: Harborlight Cosmetics</div>
    <div class="abs t" style="left:7px;top:17px;width:236px">Harborlight Cosmetics was established during 2017 to provide growth capital to brands operating in the personal care category in the final stages of launching a beauty brand in GCC.</div>
    <div class="nbar" style="left:7px;top:30px;width:124px;height:20px"><div class="d alt" style="background:var(--ink)"><div style="font-size:3.3px;color:#fff">About the Brand</div><div class="t">Ranked as No. 1 brand in the world in 2017</div></div><div class="n" style="width:16px;background:#fff;color:var(--ink);border:.5px solid #333">1</div></div>
    <div class="nbar" style="left:7px;top:52px;width:124px;height:20px"><div class="d alt" style="background:var(--ink-2)"><div style="font-size:3.3px;color:#fff">About the Product</div><div class="t">Product portfolio of 300 SKUs with award winning products</div></div><div class="n" style="width:16px;background:#fff;color:var(--ink);border:.5px solid #333">2</div></div>
    <div class="nbar" style="left:7px;top:74px;width:124px;height:20px"><div class="d"><div style="font-size:3.3px;color:#fff">Distribution Overview</div><div class="t">Established in Thailand in 1994 by a visionary entrepreneur</div></div><div class="n" style="width:16px;background:#fff;color:var(--ink);border:.5px solid #333">3</div></div>
    <div class="nbar" style="left:7px;top:96px;width:124px;height:20px"><div class="d alt" style="background:#555"><div style="font-size:3.3px;color:#fff">Harborlight Value Add</div><div class="t">Secured exclusive rights for GCC and Levant in 2017</div></div><div class="n" style="width:16px;background:#fff;color:var(--ink);border:.5px solid #333">4</div></div>
    <div class="abs" style="left:140px;top:31px;font-size:3.2px;font-weight:700">GCC Planned Retail Development 2017-2020</div>
    <div class="photo" style="left:145px;top:40px;width:95px;height:70px;background:linear-gradient(160deg,#d6d6d8,#a2a2a4)" role="img" aria-label="Map of GCC with planned store locations"></div>
    <div class="foot"><span class="mark">HARBORLIGHT</span><span>© Copyright 2017 HARBORLIGHT EQUITY. All rights reserved.</span></div>
  </section>
  <section class="slide dark divider">
    <div class="photo ph-crowd" style="left:0;top:0;width:252px;height:141px" role="img" aria-label="Business handshake in a modern office"></div>
    <div class="brand"><span class="sq"></span>HARBORLIGHT</div>
    <div class="sec"><b>SECTION 3 :</b><span>WHY PARTNERING WITH US?</span></div>
    <div class="stripe"></div>
  </section>
</div>

<div class="row">
  <section class="slide">
    <div class="title">Why Partner with Harborlight Equity?</div>
    <svg class="abs" style="left:0;top:0" width="252" height="141" viewBox="0 0 252 141">
      <path d="M110 30 A50 50 0 0 1 110 125" fill="none" stroke="#ccc" stroke-width=".6"/>
    </svg>
    <div class="circ" style="left:141px;top:22px"></div>
    <div class="circ" style="left:118px;top:42px"></div>
    <div class="circ" style="left:105px;top:62px"></div>
    <div class="circ" style="left:108px;top:84px"></div>
    <div class="circ" style="left:122px;top:104px"></div>
    <div class="photo" style="left:166px;top:38px;width:38px;height:40px;background:linear-gradient(180deg,#eee,#bbb)" role="img" aria-label="Handshake illustration"></div>
    <div class="abs" style="left:188px;top:80px;display:flex;gap:2px;align-items:center;font-size:3.5px;font-weight:700"><span style="width:5px;height:5px;border:.6px solid var(--ink)"></span>HARBORLIGHT</div>
    <div class="abs" style="left:25px;top:21px;width:112px;text-align:right;font-size:3px"><b class="red">Growth Capital</b><div class="t">Ability to finance market entry strategies in emerging markets</div></div>
    <div class="abs" style="left:10px;top:42px;width:104px;text-align:right;font-size:3px"><b class="red">Regional Access</b><div class="t">Reach into GCC, Egypt, India and Pakistan. Close relationships with key local stakeholders</div></div>
    <div class="abs" style="left:5px;top:62px;width:96px;text-align:right;font-size:3px"><b class="red">Expertise and Knowledge</b><div class="t">+100 years of growth capital investment. Diverse and dedicated team</div></div>
    <div class="abs" style="left:5px;top:84px;width:100px;text-align:right;font-size:3px"><b class="red">Track Record</b><div class="t">Robust expertise in investing into emerging consumer brands</div></div>
    <div class="abs" style="left:10px;top:104px;width:110px;text-align:right;font-size:3px"><b class="red">Operational Expertise</b><div class="t">Success model focused on active investor approach across retail</div></div>
    <div class="foot"><span class="mark">HARBORLIGHT</span><span>© Copyright 2017 HARBORLIGHT EQUITY. All rights reserved.</span></div>
  </section>
  <section class="slide">
    <div class="title">An Experienced Investor in Emerging Markets</div>
    <div class="abs" style="left:7px;top:18px;width:238px;height:13px;background:var(--ink);color:#fff;font-size:3px;padding:2px 4px">Harborlight Equity has advised on more than USD 2 billion of transaction value in the last 5 years, with a significant exposure to retail, FMCG, E-Commerce and other consumer products in MENA region</div>
    <div class="logo-box" style="left:14px;top:38px"></div><div class="logo-box" style="left:43px;top:38px"></div><div class="logo-box" style="left:72px;top:38px"></div><div class="logo-box" style="left:101px;top:38px"></div>
    <div class="logo-box" style="left:130px;top:38px"></div><div class="logo-box" style="left:159px;top:38px"></div><div class="logo-box" style="left:188px;top:38px"></div><div class="logo-box" style="left:217px;top:38px"></div>
    <div class="abs t" style="left:12px;top:53px;width:230px;word-spacing:9px">Advisory Sale Advisory Growth Advisory Equity Buyout Advisory Sale</div>
    <div class="logo-box" style="left:14px;top:76px"></div><div class="logo-box" style="left:43px;top:76px"></div><div class="logo-box" style="left:72px;top:76px"></div><div class="logo-box" style="left:101px;top:76px"></div>
    <div class="logo-box" style="left:130px;top:76px"></div><div class="logo-box" style="left:159px;top:76px"></div><div class="logo-box" style="left:188px;top:76px"></div><div class="logo-box" style="left:217px;top:76px"></div>
    <div class="abs t" style="left:12px;top:91px;width:230px;word-spacing:9px">Advisory Sale Advisory Growth Advisory Equity Buyout Advisory Sale</div>
    <div class="abs" style="left:7px;top:114px;width:238px;height:1px;background:var(--red)"></div>
    <div class="foot"><span class="mark">HARBORLIGHT</span><span>© Copyright 2017 HARBORLIGHT EQUITY. All rights reserved.</span></div>
  </section>
  <section class="slide dark divider">
    <div class="photo ph-crowd" style="left:0;top:0;width:252px;height:141px" role="img" aria-label="Young people in a crowd at a concert"></div>
    <div class="brand"><span class="sq"></span>HARBORLIGHT</div>
    <div class="sec"><b>SECTION 3 :</b><span>THE MILLENNIAL CONSUMER</span></div>
    <div class="stripe"></div>
  </section>
</div>

<div class="row">
  <section class="slide">
    <div class="title">Consumer Fundamentals in MENA and BRIC Markets</div>
    <div class="tile" style="left:8px;top:20px"><b>4.2</b><span>Billion people from BRIC by 2025</span></div>
    <div class="tile" style="left:68px;top:20px"><b>36%</b><span>Of global GDP for BRIC (2015-2030)</span></div>
    <div class="tile" style="left:128px;top:20px"><b>50%</b><span>Of the global consumption from BRIC</span></div>
    <div class="tile" style="left:188px;top:20px"><b>30 years</b><span>Median age in BRIC (2017)</span></div>
    <div class="tile dk" style="left:8px;top:66px"><b>USD 9,040</b><span>GDP per capita in MENA region (2017)</span></div>
    <div class="tile dk" style="left:68px;top:66px"><b>2%</b><span>Of Northgate revenue are from MENA</span></div>
    <div class="tile dk" style="left:128px;top:66px"><b>380</b><span>Million inhabitants in MENA (2017)</span></div>
    <div class="tile dk" style="left:188px;top:66px"><b>6%</b><span>Of Global GDP contribution from MENA (2017)</span></div>
    <div class="foot"><span class="mark">HARBORLIGHT</span><span>© Copyright 2017 HARBORLIGHT EQUITY. All rights reserved.</span></div>
  </section>
  <section class="slide">
    <div class="title">Consumer Profiling Insights</div>
    <div class="abs" style="left:7px;top:19px;font-size:3.5px;font-weight:700">Who are they?</div>
    <svg class="abs" style="left:7px;top:25px" width="50" height="12" viewBox="0 0 50 12">
      <g fill="var(--red)"><circle cx="3" cy="2" r="1.5"/><circle cx="9" cy="2" r="1.5"/><circle cx="15" cy="2" r="1.5"/><circle cx="21" cy="2" r="1.5"/><circle cx="27" cy="2" r="1.5"/><circle cx="33" cy="2" r="1.5"/><circle cx="39" cy="2" r="1.5"/><circle cx="45" cy="2" r="1.5"/>
      <rect x="1.5" y="4" width="3" height="7"/><rect x="7.5" y="4" width="3" height="7"/><rect x="13.5" y="4" width="3" height="7"/><rect x="19.5" y="4" width="3" height="7"/><rect x="25.5" y="4" width="3" height="7"/><rect x="31.5" y="4" width="3" height="7"/><rect x="37.5" y="4" width="3" height="7"/><rect x="43.5" y="4" width="3" height="7"/></g>
    </svg>
    <div class="abs" style="left:60px;top:24px;font-size:3px;font-weight:700">BORN BETWEEN<br><span style="font-size:6px">1980 – 2000</span></div>
    <div class="abs t" style="left:7px;top:42px;width:90px"><b style="color:#222">Searching for Value for Money</b><br>Quality is still key for millennials, but price is a more important factor than it is for other generations.</div>
    <svg class="abs" style="left:7px;top:66px" width="90" height="58" viewBox="0 0 90 58">
      <text x="0" y="10" font-size="3" fill="var(--red)">Price</text><text x="0" y="42" font-size="3">Quality</text>
      <rect x="20" y="2" width="16" height="24" fill="var(--red)"/><rect x="20" y="28" width="16" height="26" fill="#111"/>
      <rect x="55" y="2" width="16" height="24" fill="var(--red)"/><rect x="55" y="28" width="16" height="26" fill="#111"/>
      <text x="23" y="15" font-size="3" fill="#fff">48%</text><text x="58" y="15" font-size="3" fill="#fff">40%</text>
      <text x="23" y="43" font-size="3" fill="#fff">52%</text><text x="58" y="43" font-size="3" fill="#fff">60%</text>
    </svg>
    <div class="abs t" style="left:106px;top:19px;width:136px"><b style="color:#222">Clicking to buy</b><br>Millennials' affinity for technology is reshaping the retail space.</div>
    <div class="abs" style="left:106px;top:36px;width:100px;height:5px;background:#ddd"><div style="width:87%;height:100%;background:var(--red)"></div></div>
    <div class="abs red" style="left:210px;top:33px;font-size:6px;font-weight:700">87%</div>
    <div class="abs t" style="left:106px;top:48px;width:136px"><b style="color:#222">The Power of Social</b><br><span class="red" style="font-size:6px;font-weight:700">34%</span> aged between 18 to 34 like a brand more when that brand uses social media</div>
    <div class="abs" style="left:106px;top:70px;width:80px;height:5px;background:#ddd"><div style="width:34%;height:100%;background:var(--red)"></div></div>
    <div class="abs" style="left:200px;top:68px;display:flex;gap:2px"><span style="width:6px;height:6px;border-radius:50%;background:#555"></span><span style="width:6px;height:6px;border-radius:50%;background:#555"></span><span style="width:6px;height:6px;border-radius:50%;background:#555"></span></div>
    <div class="abs t" style="left:106px;top:86px;width:136px"><b style="color:#222">Spending v/s Saving</b><br>The majority of millennials have less than <span class="red" style="font-size:5px;font-weight:700">USD 1,000</span> in their savings accounts, and a significant number have nothing at all.</div>
    <div class="foot"><span class="mark">HARBORLIGHT</span><span>© Copyright 2017 HARBORLIGHT EQUITY. All rights reserved.</span></div>
  </section>
  <section class="slide">
    <div class="title">Retail and Consumer Sector Key Insights</div>
    <div class="abs" style="left:7px;top:18px;font-size:3.3px;font-weight:700">USD 399 Bn opportunity growing at a 6% CAGR</div>
    <svg class="abs" style="left:40px;top:30px" width="70" height="70" viewBox="0 0 42 42">
      <circle cx="21" cy="21" r="15.9" fill="none" stroke="var(--red)" stroke-width="10" stroke-dasharray="40 60" transform="rotate(-90 21 21)"/>
      <circle cx="21" cy="21" r="15.9" fill="none" stroke="#888" stroke-width="10" stroke-dasharray="25 75" stroke-dashoffset="-40" transform="rotate(-90 21 21)"/>
      <circle cx="21" cy="21" r="15.9" fill="none" stroke="#444" stroke-width="10" stroke-dasharray="20 80" stroke-dashoffset="-65" transform="rotate(-90 21 21)"/>
      <circle cx="21" cy="21" r="15.9" fill="none" stroke="#bbb" stroke-width="10" stroke-dasharray="15 85" stroke-dashoffset="-85" transform="rotate(-90 21 21)"/>
    </svg>
    <div class="abs t" style="left:10px;top:44px;width:30px">Apparel<br>Footwear<br>Beauty<br>Home</div>
    <div class="abs" style="left:170px;top:18px;font-size:3.3px;font-weight:700">A disruptive operating model</div>
    <svg class="abs" style="left:150px;top:26px" width="96" height="30" viewBox="0 0 96 30">
      <g fill="none" stroke="var(--red)" stroke-width="1.5"><circle cx="12" cy="15" r="8"/><circle cx="36" cy="15" r="8"/><circle cx="60" cy="15" r="8"/><circle cx="84" cy="15" r="8"/></g>
      <g fill="#333"><circle cx="12" cy="15" r="3"/><circle cx="36" cy="15" r="3"/><circle cx="60" cy="15" r="3"/><circle cx="84" cy="15" r="3"/></g>
    </svg>
    <div class="abs" style="left:168px;top:60px;font-size:3.3px;font-weight:700">Offers high growth investment options</div>
    <svg class="abs" style="left:150px;top:66px" width="96" height="54" viewBox="0 0 96 54">
      <path d="M8 48 H92 M8 48 V4" stroke="#333" stroke-width=".6"/>
      <circle cx="30" cy="36" r="3" fill="#444"/><circle cx="46" cy="28" r="4" fill="#888"/><circle cx="62" cy="22" r="3" fill="#444"/><circle cx="78" cy="14" r="6" fill="var(--red)"/>
      <text x="34" y="53" font-size="3">Historic Growth Rate (%)</text>
    </svg>
    <div class="foot"><span class="mark">HARBORLIGHT</span><span>© Copyright 2017 HARBORLIGHT EQUITY. All rights reserved.</span></div>
  </section>
</div>

<div class="row">
  <section class="slide dark">
    <div class="photo ph-city" style="left:0;top:0;width:252px;height:141px" role="img" aria-label="Dark city backdrop"></div>
    <div class="band" style="left:126px;top:0;width:44px;height:141px"></div>
    <div class="brand abs" style="left:176px;top:66px;font-size:4.5px"><span class="sq"></span>HARBORLIGHT</div>
    <div class="abs" style="left:33px;top:16px;font-size:9px;letter-spacing:.5px">CONTACTS</div>
    <div class="abs" style="left:32px;top:40px;font-size:3.8px;line-height:1.4;color:#eee">
      Harborlight Equity Ltd.<br>Contact: 00000 555 0101<br>Email: <u>lara@harborlightpartners.example</u><br><br>
      Harborlight Partners &amp; Co LLC<br>Contact: 00000 555 0102<br>Email: <u>nadia@harborlightpartners.example</u><br><br>
      Harborlight Urban Footwear Trading<br>Contact: 00000 555 0103<br>Email: <u>peter@harborlightpartners.example</u>
    </div>
  </section>
  <section class="slide dark">
    <div class="photo ph-city" style="left:0;top:0;width:252px;height:141px" role="img" aria-label="City skyline at night"></div>
    <div class="band" style="left:0;top:0;width:120px;height:141px;opacity:.85"></div>
    <div class="abs" style="left:16px;top:63px;font-size:9px;letter-spacing:.3px">THANK YOU</div>
    <div class="brand abs" style="left:130px;top:62px;font-size:7px"><span class="sq" style="width:13px;height:13px"></span>HARBORLIGHT</div>
  </section>
</div>

</main>
</body>
</html>
```